Sacred Anointing Oils need new label

Beautiful sacred oils need a new label. There are 4 oils with 4 key colours. The labels need to match together, so they look good on a shop shelf. They have a feeling of warmth, simplicity, beauty, non religious, yet sacred. Engaging. I have now created a photoshop mockup of what I like and will attach the psd files.
I will attach the current cards to give you more of a feel of the oils. There is not a card yet for Halbrey. The cards will also need to be changed, as another project, once the labels are completed.

There are 4 Oils, Spikenard, Verolinde, Halbrey, Amber Hush. They each have matching cards to go with them. The labels go on 15ml cobalt blue glass bottles. The size is 85mm x 42mm including bleed. I need them laid out on an A4 sheet, I can fit 12 per page. Slightly rounded corners. Each bottle is the same layout, different colour scheme. Header font is Apple chancery.

Target Market(s)

Women 15-80

Industry/Entity Type

Shop

Contact Information for Business Card

Please see attached information and logo

Font styles to use
Other font styles liked:
• There will be simple san serif font for the contents details. the title name eg Verolinde can be more script or decorative. I have used QumpellikaNo12 in the past, and Apple Chancery. am open to similar options.

Requirements
Must have
• 4 labels are attached with the mockup design of what I want. Must be
• clear and easy to read, a feeling of warmth, rich colours. Must be one label per bottle (not two), rectangular wrapping around bottle. Not 2 labels per bottle. The label size must be 42mm height and a minimum of 88mm in length around bottle - this includes bleed. The actual height of the label, without bleed must be a maximum of 37mm and width 89mm max.
Nice to have
• The image from logo needs to be eye catching and drawing people in, a sense of flow.
Should not have
• Must not be clunky, hard to read, two labels. No religious imagery

```html
<!DOCTYPE html>
<html lang="en">
<head>
<meta charset="utf-8">
<title>Anointing Oil Labels</title>
<link rel="stylesheet" href="https://fonts.googleapis.com/css2?family=Playball&family=Cinzel:wght@400&family=PT+Sans:wght@400;700&display=swap">
<style>
  :root {
    --page-bg: #2b2b2b;
    --cream: #f7dcb8;
    --cream-soft: #ecc9a2;
    --ink: #ffffff;
    --panel-text: #1c1c1c;
    --mark: #c98fc0;

    --verolinde-top: #8b1f25;
    --verolinde-bottom: #d80f1f;
    --verolinde-strip: #9e0f1f;

    --amber-top: #c6143f;
    --amber-bottom: #ef5c22;
    --amber-strip: #b8173a;

    --spikenard-top: #6a2b22;
    --spikenard-bottom: #2a1352;
    --spikenard-strip: #8d1228;

    --halbrey-top: #481c52;
    --halbrey-bottom: #b8432a;
    --halbrey-strip: #8d1a2e;

    --script: "Playball", cursive;
    --serif: "Cinzel", serif;
    --sans: "PT Sans", sans-serif;
  }
  * { box-sizing: border-box; margin: 0; padding: 0; }
  html, body { width: 1200px; height: 900px; overflow: hidden; }
  body { background: var(--page-bg); position: relative; }

  .label {
    position: absolute;
    width: 481px;
    height: 202px;
    border-bottom: 6px solid var(--strip);
    background: linear-gradient(to bottom, var(--top), var(--bottom));
    color: var(--ink);
  }
  .label--verolinde { left: 105px; top: 240px; --top: var(--verolinde-top); --bottom: var(--verolinde-bottom); --strip: var(--verolinde-strip); }
  .label--amber     { left: 614px; top: 240px; --top: var(--amber-top); --bottom: var(--amber-bottom); --strip: var(--amber-strip); }
  .label--spikenard { left: 105px; top: 458px; --top: var(--spikenard-top); --bottom: var(--spikenard-bottom); --strip: var(--spikenard-strip); }
  .label--halbrey   { left: 614px; top: 458px; --top: var(--halbrey-top); --bottom: var(--halbrey-bottom); --strip: var(--halbrey-strip); }

  /* left column: maker details */
  .details {
    position: absolute; left: 14px; top: 22px; width: 134px;
    text-align: center;
  }
  .details__name {
    font-family: var(--script); font-size: 24px; line-height: 1;
    color: var(--cream); white-space: nowrap;
  }
  .details__kind {
    font-family: var(--serif); font-size: 7.5px; color: var(--cream-soft);
    margin-top: 3px; letter-spacing: 0.2px;
  }
  .details__contact {
    font-family: var(--sans); font-size: 8px; line-height: 10.5px;
    margin-top: 12px; color: var(--ink);
  }
  .details__web { font-weight: 700; }
  .details__abn { font-family: var(--sans); font-size: 8px; margin-top: 7px; }
  .caution {
    width: 95px; height: 37px; margin: 12px auto 0;
    background: #fff; border-radius: 6px;
    box-shadow: 0 0 0 2px #fff, 0 0 0 3px var(--strip);
    text-align: left; padding: 5px 7px;
    font-family: var(--sans); font-size: 6px; line-height: 8.5px;
    color: var(--panel-text);
  }

  /* centre column: title and mark */
  .front {
    position: absolute; left: 160px; top: 12px; width: 168px;
    text-align: center;
  }
  .front__name {
    font-family: var(--script); font-size: 36px; line-height: 1.05;
    color: var(--cream); white-space: nowrap;
  }
  .front__kind {
    font-family: var(--serif); font-size: 13px; color: var(--cream-soft);
    margin-top: 5px; letter-spacing: 0.3px;
  }
  .brand { margin-top: 8px; }
  .brand__dot { display: block; margin: 0 auto; }
  .brand__name {
    font-family: var(--serif); font-size: 15px; letter-spacing: 3px;
    color: var(--cream); margin-top: 14px;
  }

  /* right column: ingredients */
  .contents {
    position: absolute; left: 349px; top: 37px; width: 128px;
    font-family: var(--sans); font-size: 10.5px; line-height: 12.6px;
    color: var(--ink);
  }
  .contents--low { top: 44px; }
  .contents--mid { top: 39px; }
  .contents__heading { font-size: 10px; }
  .contents strong { font-weight: 700; }
</style>
</head>
<body>

<section class="label label--verolinde">
  <div class="details">
    <p class="details__name">Verolinde</p>
    <p class="details__kind">OIL OF ANOINTING</p>
    <p class="details__contact"><span class="details__web">LumenVessel.example</span><br>Tel. +61 400 182 736<br>14 Wattle Lane, Brookvale.<br>NSW, 2100, AUSTRALIA</p>
    <p class="details__abn">ABN 51 208 736 415</p>
    <div class="caution">FOR EXTERNAL USE ONLY.<br>Store away from heat &amp; light.<br>USE BY:</div>
  </div>
  <div class="front">
    <p class="front__name">Verolinde</p>
    <p class="front__kind">OIL OF ANOINTING</p>
    <div class="brand">
      <svg class="brand__dot" width="56" height="56" viewBox="0 0 56 56"><circle cx="28" cy="28" r="26" fill="var(--mark)"/></svg>
      <p class="brand__name">LUMEN VESSEL</p>
    </div>
  </div>
  <div class="contents">
    <p class="contents__heading">CONTENTS</p>
    <p><strong>Organic oils:</strong></p>
    <p>Punica granatum,<br>Simmondia chinensis,<br>Limnanthes alba,<br>Rosa,<br>Ravansara aromatica,<br>Chrysopogon zizanoides,<br>Cymbopogon,<br>Pelargonium graveolens.<br><strong>Essences.</strong></p>
  </div>
</section>

<section class="label label--amber">
  <div class="details">
    <p class="details__name">Amber Hush</p>
    <p class="details__kind">OIL OF ANOINTING</p>
    <p class="details__contact"><span class="details__web">LumenVessel.example</span><br>Tel. +61 400 182 736<br>14 Wattle Lane, Brookvale.<br>NSW, 2100, AUSTRALIA</p>
    <p class="details__abn">ABN 51 208 736 415</p>
    <div class="caution">FOR EXTERNAL USE ONLY.<br>Store away from heat &amp; light.<br>USE BY:</div>
  </div>
  <div class="front">
    <p class="front__name">Amber Hush</p>
    <p class="front__kind">OIL OF ANOINTING</p>
    <div class="brand">
      <svg class="brand__dot" width="56" height="56" viewBox="0 0 56 56"><circle cx="28" cy="28" r="26" fill="var(--mark)"/></svg>
      <p class="brand__name">LUMEN VESSEL</p>
    </div>
  </div>
  <div class="contents contents--low">
    <p class="contents__heading">CONTENTS:</p>
    <p><strong>Organic oils:</strong></p>
    <p>Helianthus annua,<br>Artemisia vulgaris,<br>Matricaria chamomilla,<br>Cedrus atlantica,<br>Salvia sclarea,<br>Evernia prunastri,<br>Zingiber off.<br><strong>Essences.</strong></p>
  </div>
</section>

<section class="label label--spikenard">
  <div class="details">
    <p class="details__name">Spikenard</p>
    <p class="details__kind">OIL OF ANOINTING</p>
    <p class="details__contact"><span class="details__web">LumenVessel.example</span><br>Tel. +61 400 182 736<br>14 Wattle Lane, Brookvale.<br>NSW, 2100, AUSTRALIA</p>
    <p class="details__abn">ABN 51 208 736 415</p>
    <div class="caution">FOR EXTERNAL USE ONLY.<br>Store away from heat &amp; light.<br>USE BY:</div>
  </div>
  <div class="front">
    <p class="front__name">Spikenard</p>
    <p class="front__kind">OIL OF ANOINTING</p>
    <div class="brand">
      <svg class="brand__dot" width="56" height="56" viewBox="0 0 56 56"><circle cx="28" cy="28" r="26" fill="var(--mark)"/></svg>
      <p class="brand__name">LUMEN VESSEL</p>
    </div>
  </div>
  <div class="contents contents--mid">
    <p class="contents__heading">CONTENTS:</p>
    <p><strong>Organic Oils:</strong></p>
    <p>Simmondia chinensis,<br>Nardostachys<br>grandiflora.<br><strong>Essences</strong> of Rose,<br>Gold,<br>Willowmere Spring,<br>Pink Flannel Flower,<br>Helichrysum.</p>
  </div>
</section>

<section class="label label--halbrey">
  <div class="details">
    <p class="details__name">Halbrey</p>
    <p class="details__kind">OIL OF ANOINTING</p>
    <p class="details__contact"><span class="details__web">LumenVessel.example</span><br>Tel. +61 400 182 736<br>14 Wattle Lane, Brookvale.<br>NSW, 2100, AUSTRALIA</p>
    <p class="details__abn">ABN 51 208 736 415</p>
    <div class="caution">FOR EXTERNAL USE ONLY.<br>Store away from heat &amp; light.<br>USE BY:</div>
  </div>
  <div class="front">
    <p class="front__name">Amber Hush</p>
    <p class="front__kind">OIL OF ANOINTING</p>
    <div class="brand">
      <svg class="brand__dot" width="56" height="56" viewBox="0 0 56 56"><circle cx="28" cy="28" r="26" fill="var(--mark)"/></svg>
      <p class="brand__name">LUMEN VESSEL</p>
    </div>
  </div>
  <div class="contents contents--mid">
    <p class="contents__heading">CONTENTS:</p>
    <p><strong>Organic oils:</strong></p>
    <p>Prunus armeniaca,<br>Simmondia chinensis,<br>Evernia prunastri,<br>Aquilaria sp,<br>Helichrysum italicum,<br>Rosa so,<br>Pelargonium sp.<br><strong>Essences.</strong></p>
  </div>
</section>

</body>
</html>
```